Brightwell Home Care Site Redesign

SIte redesign for a commercial/residential cleaning and restoration company.

Design style should be as for a professional service company. Use this as a guide: https://lumora.sitecraftery.com/plumber/

Please use current site content located here: http://bhcqrx.com/

Design should be responsive

Site Design should include two (2) pages:
- Homepage
- Interior page (for services) with a layout that can be duplicated across the different interior pages

Please Use the following items for the Navigation:
• Water Damage Restoration
• Fire & Smoke Damage Restoration
• Remodeling
• Roofing
• New Flooring Sales and Installation
• 24HR Emergency Services
• Commercial Services

Add BOLD, red Call To Action of "CALL NOW" on homepage

Feature image to be around water damage restoration and emergency services (flooded home) – similar to this photo: http://bhcqrx.com/images/flood.jpg

Add work and projects section

Keep services icons and descriptions with main focus is Water damage, Fire damage, Storm damage, Roof repair replacement, Exterior repairs and Kitchen/Bath Remodeling

Target Market(s)

Customers looking for home disaster restoration services

Number of Pages Required

2 page

Requirements
Must have
• Responsive Design
• 2 pages submitted - Homepage & Interior page. Designs WILL NOT be considered if 2 pages aren't submitted

```html
<!DOCTYPE html>
<html lang="en">
<head>
<meta charset="utf-8">
<title>Brightwell Home Care</title>
<link href="https://fonts.googleapis.com/css2?family=Work+Sans:wght@300;400;500;600;700&display=swap" rel="stylesheet">
<style>
:root{
  --navy:#1a1a8c;
  --ink:#3a3a3a;
  --muted:#666;
  --red:#e0262b;
  --line:#e6e6e6;
  --white:#fff;
  --drop:rgba(28,28,28,.88);
}
*{box-sizing:border-box;margin:0;padding:0}
html,body{width:1120px;height:1200px;overflow:hidden;background:var(--white)}
body{font-family:"Work Sans",sans-serif;color:var(--ink);position:relative}
.abs{position:absolute}

.site-header{left:0;top:0;width:1120px;height:62px;background:var(--white);box-shadow:0 2px 3px rgba(0,0,0,.15);z-index:3}
.brand{left:178px;top:24px;width:120px;font-size:13px;line-height:15px;font-weight:700;color:var(--navy);display:flex;align-items:center;gap:7px;letter-spacing:.2px}
.brand i{width:12px;height:12px;background:var(--navy);display:block;flex:none}
.nav a{position:absolute;top:35px;font-size:12px;letter-spacing:.5px;color:#555;text-decoration:none;text-transform:uppercase;white-space:nowrap}
.nav .active{border-bottom:2px solid var(--navy);padding-bottom:8px;color:#444}
.nav .open{color:var(--navy)}

.hero{left:0;top:62px;width:1120px;height:310px;background:linear-gradient(180deg,#9a9788 0%,#8d8f83 45%,#6f7a71 75%,#7d8780 100%)}
.hero-title{left:0;width:1120px;top:104px;text-align:center;color:var(--white);font-weight:300;font-size:44px;letter-spacing:1px}
.hero-sub{left:0;width:1120px;text-align:center;color:var(--white);font-size:18px;letter-spacing:1px}
.hero-tag{left:0;width:1120px;top:200px;text-align:center;color:var(--white);font-size:12px;letter-spacing:1px}
.arrow{top:203px;font-size:26px;line-height:1}
.cta{left:439px;top:266px;width:242px;height:58px;background:var(--red);color:var(--white);font-weight:700;font-size:22px;letter-spacing:.5px;display:flex;align-items:center;justify-content:center;z-index:2}

.dropdown{left:538px;top:62px;width:229px;height:208px;background:var(--drop);z-index:2;padding-top:0}
.dropdown a{display:block;padding:0 16px;height:28.8px;line-height:28.8px;color:var(--white);font-size:8.8px;font-weight:500;text-decoration:none;letter-spacing:.2px;white-space:nowrap}

.feature{top:410px;width:260px;text-align:center}
.feature h3{font-size:15px;font-weight:400;letter-spacing:.4px;margin:14px 0 8px;color:#333}
.feature p{font-size:9px;line-height:11.5px;color:var(--muted)}
.feature b{color:#222}
.vsep{top:423px;width:1px;height:88px;background:var(--line)}
.hr{left:178px;width:766px;height:1px;background:var(--line)}

.area-title{left:178px;top:574px;font-size:19px;color:var(--navy);font-weight:400;letter-spacing:.3px}
.col{font-size:9.3px;line-height:19.2px;color:#444;letter-spacing:.2px}
.col p+p{margin-top:19.2px}

.box{top:846px;height:198px;border:1px solid var(--line)}
.checklist{list-style:none;padding:13px 0 0 20px}
.checklist li{font-size:9.3px;line-height:19.2px;color:#444}
.checklist li::before{content:"• "}
.lorem{left:22px;top:12px;width:180px;font-size:9.3px;line-height:19.2px;color:#444}
.lorem p+p{margin-top:19.2px}
.video{left:212px;top:14px;width:240px;height:166px;background:linear-gradient(160deg,#111 0%,#2a0d0d 60%,#111 100%)}

.photo{height:200px}
</style>
</head>
<body>

<header class="site-header abs">
  <div class="brand abs"><i></i><span>Brightwell<br>Home Care</span></div>
  <nav class="nav">
    <a class="active" style="left:328px">Home</a>
    <a style="left:429px">About Us</a>
    <a class="open" style="left:555px">Services ▾</a>
    <a style="left:678px">Blog</a>
    <a style="left:767px">555-014-227</a>
    <a style="left:856px">555-014-8836</a>
  </nav>
</header>

<section class="hero abs" role="img" aria-label="Flooded living room with furniture standing in water"></section>
<div class="hero-title abs">32 YEARS EXPERIENCE</div>
<div class="hero-sub abs" style="top:158px">FLOOD SERVICE 24 HOURS</div>
<div class="hero-sub abs" style="top:177px">7 DAYS A WEEK</div>
<div class="hero-tag abs">SPECIALIZING IN EMERGENCY FLOOD SERVICES AND MORE!</div>
<div class="arrow abs" style="left:176px;color:var(--red)">❬</div>
<div class="arrow abs" style="left:934px;color:var(--white)">❭</div>
<a class="cta abs">CALL NOW</a>

<nav class="dropdown abs">
  <a>WATER DAMAGE RESTORATION</a>
  <a>FIRE &amp; SMOKE DAMAGE RESTORATION</a>
  <a>REMODELING</a>
  <a>ROOFING</a>
  <a>NEW FLOORING SALES AND INSTALLATION</a>
  <a>24HR EMERGENCY SERVICES</a>
  <a>COMMERCIAL SERVICES</a>
</nav>

<section>
  <div class="feature abs" style="left:156px">
    <svg width="28" height="28" viewBox="0 0 28 28" fill="none" stroke="#1a1a8c" stroke-width="1.6"><rect x="9" y="2" width="10" height="24"/><rect x="2" y="12" width="7" height="14"/><rect x="19" y="12" width="7" height="14"/><path d="M12 6h4M12 10h4M12 14h4M12 18h4M4 16v6M23 16v6"/></svg>
    <h3>Commercial Services</h3>
    <p>We have special rates and services for commer-<br>cial clients. <b>Contact us for a quote»</b></p>
  </div>
  <div class="vsep abs" style="left:438px"></div>
  <div class="feature abs" style="left:436px">
    <svg width="28" height="28" viewBox="0 0 28 28" fill="none" stroke="#1a1a8c" stroke-width="1.6"><path d="M15 3h9v9L12 24 4 16z"/><circle cx="20" cy="7" r="1.4"/><path d="M11 17l5-5"/></svg>
    <h3>Get Pricing</h3>
    <p>Request pricing and apply for your online<br>discount code.</p>
  </div>
  <div class="vsep abs" style="left:698px"></div>
  <div class="feature abs" style="left:710px">
    <svg width="28" height="28" viewBox="0 0 28 28" fill="none" stroke="#1a1a8c" stroke-width="1.6"><path d="M2 2v24h24V19h-6v-5h-5V9H9V2z"/><path d="M17 3l7 7M20 10h4V6"/></svg>
    <h3>Emergency Service</h3>
    <p>Fires and Floods rarely wait until it is conve-<br>nient. This is why we are available 24 hours a<br>day to handle your emergency.<br><b>Contact us now»</b></p>
  </div>
</section>

<div class="hr abs" style="top:554px"></div>

<section>
  <h2 class="area-title abs">Service Area</h2>
  <div class="col abs" style="left:178px;top:617px;width:240px">
    <p>Brightwell Home Care provides service to all of the Dallas/Fort Worth metroplex area including</p>
    <p>Dallas, Plano, Garland, Frisco, Rockwall, Rowlett, Carrollton, Coppell, Addison, Highland Park, University Park, Grand Prairie, and more. Call or Email us today to find out if you are in our service area.</p>
  </div>
  <div class="col abs" style="left:474px;top:612px;width:240px">
    <p>Brightwell Home Care is more than just a carpet clean-ing company.</p>
    <p>Our customers also count on us for tile and grout cleaning, upholstery cleaning, carpet repa2ir, stain removal, flood and fire damage restoration. Always on call, we are ready to spring into action 24 hours a day if you need emergency service. Moreover, we provide full service carpet and tile</p>
  </div>
  <div class="col abs" style="left:761px;top:611px;width:190px">
    <p>Thank you for your interest in Brightwell Home Care! You can reach us via phone or E-Mail for pricing, availability, and addi-tional services.</p>
    <p>Dallas: 555-014-2271<br>DFW Suburbs: 555-014-2271<br>E-Mail: hello@brightwell-care.net</p>
  </div>
</section>

<div class="hr abs" style="top:812px"></div>

<section>
  <div class="box abs" style="left:176px;width:266px">
    <ul class="checklist">
      <li>Lowest prices.</li>
      <li>Quick and efficient services.</li>
      <li>Availability throughout Melbourne.</li>
      <li>Licensed, certified, and trained cleaners.</li>
      <li>32 years of industry experience.</li>
      <li>Eco-friendly cleaning solutions.</li>
      <li>Latest cleaning tools.</li>
      <li>Same day carpet restoration services.</li>
      <li>Guaranteed results.</li>
    </ul>
  </div>
  <div class="box abs" style="left:474px;width:470px">
    <div class="lorem abs">
      <p>Lorem ipsum dolor sit amet, consectetur adipiscing elit. Aenean enim purus, imperdiet e</p>
      <p>get blandit tempor, mattis nec erat. Suspendisse tincidunt justo nunc, sed pulvinar viverra urna.</p>
      <p>Sed tristique odio arcu, nec &nbsp;Quis</p>
    </div>
    <div class="video abs" role="img" aria-label="Video about DuctSweep duct cleaning equipment"></div>
  </div>
</section>

<section>
  <div class="photo abs" style="left:174px;top:1094px;width:230px;background:linear-gradient(135deg,#cbbfa3,#a89a7f)" role="img" aria-label="Technician cleaning an upholstered armchair"></div>
  <div class="photo abs" style="left:450px;top:1070px;width:230px;background:linear-gradient(135deg,#4a3c30,#7a6550)" role="img" aria-label="Worker installing wood flooring"></div>
  <div class="photo abs" style="left:715px;top:1102px;width:230px;background:linear-gradient(160deg,#2c5fa8,#8fb4de 55%,#3d6ea3)" role="img" aria-label="Glass commercial office towers"></div>
</section>

</body>
</html>
```